Brett Olsen Building Business Card Design

Hi,

I need a business card for my Building company.
I am a Builder and build homes for clients.
I am looking for a sophisticated logo that can be used on business cards, envelopes and letter heads.
I am trying to take my business to the next level and need a professional business card.

Colours: Please use white, black, dark grey and bright blue.

Thank you,

Carol and Brett.

Target Market(s)

1. Home and Building Companies 2. Potential customers

Industry/Entity Type

Business

Contact Information for Business Card

Brett Olsen Building PTY LTD

Brett Olsen

Director

A.B.N. 37 829 516 073

BUILDERS LICENCE No. 573019k

Mobile: 0412 907 381

Email: brettolsenbuilding@mailvane.com.au

Requirements
Must have
• The following is compulsory to have in the designs:

Brett Olsen Building PTY LTD (business name)

Brett Olsen (contact name)

Director (position)

A.B.N. 37 829 516 073

Builders Licence No. 573019k

Mobile: 0412 907 381

Nice to have
• Logo for business
Should not have
• Should not be cluttered.

I am looking for a clean, sophisticated and professional business card design.

```html
<!DOCTYPE html>
<html lang="en">
<head>
<meta charset="utf-8">
<title>Brett Olsen Building – Business Cards</title>
<link rel="stylesheet" href="https://fonts.googleapis.com/css2?family=Roboto+Slab:wght@400;700&display=swap">
<style>
  :root {
    --board: #000000;
    --white: #ffffff;
    --blue: #00adef;
    --grey: #666769;
    --ink: #111111;
    --text-grey: #58595b;
    --brand-grey: #6d6e71;
  }
  * { margin: 0; padding: 0; box-sizing: border-box; }
  html, body {
    width: 1200px; height: 815px; overflow: hidden;
    background: var(--board);
    font-family: "Roboto Slab", Georgia, serif;
  }
  .board { position: relative; width: 1200px; height: 815px; }
  .card { position: absolute; overflow: hidden; }
  .card--front-light { left: 57px; top: 95px; width: 508px; height: 281px; background: var(--white); }
  .card--front-dark { left: 605px; top: 95px; width: 510px; height: 282px; background: var(--grey); }
  .card--back-blue { left: 55px; top: 390px; width: 511px; height: 283px; background: var(--blue); }
  .card--back-dark { left: 605px; top: 390px; width: 510px; height: 283px; background: var(--grey); }

  .abs { position: absolute; white-space: nowrap; }
  .contact-name { font-weight: 700; font-size: 21px; line-height: 1; }
  .contact-role { font-size: 16px; line-height: 1; }
  .detail { font-size: 13.5px; line-height: 1; }
  .label { color: var(--blue); }

  .brand-name { font-weight: 400; line-height: 1.05; }
  .square { position: absolute; background: var(--blue); }

  /* light front */
  .card--front-light .contact-name { color: var(--ink); }
  .card--front-light .contact-role { color: var(--ink); }
  .card--front-light .detail { color: var(--text-grey); }
  .divider { position: absolute; left: 202px; top: 124px; width: 3px; height: 137px; background: var(--blue); }

  /* dark front */
  .card--front-dark .contact-name,
  .card--front-dark .contact-role,
  .card--front-dark .detail { color: var(--white); }
</style>
</head>
<body>
<div class="board">

  <!-- Front, white -->
  <section class="card card--front-light">
    <div class="square" style="left:58px; top:160px; width:14px; height:14px;"></div>
    <div class="abs brand-name" style="left:56px; top:182px; font-size:17px; color:var(--brand-grey);">Brett Olsen<br>Building</div>
    <div class="divider"></div>
    <div class="abs contact-name" style="left:223px; top:54px;">Brett Olsen</div>
    <div class="abs contact-role" style="left:224px; top:81px;">Director</div>
    <div class="abs detail" style="left:222px; top:142px;">A.B.N. 37 829 516 073</div>
    <div class="abs detail" style="left:219px; top:163px;">BUILDERS LICENCE No. 573019k</div>
    <div class="abs detail" style="left:218px; top:204px;"><span class="label">M:</span> 0412 907 381</div>
    <div class="abs detail" style="left:218px; top:235px;"><span class="label">E:</span> brettolsenbuilding@mailvane.com.au</div>
  </section>

  <!-- Front, grey -->
  <section class="card card--front-dark">
    <div class="abs brand-name" style="left:73px; top:200px; font-size:16px; color:var(--ink);">Brett Olsen<br>Building</div>
    <div class="square" style="left:50px; top:248px; width:13px; height:13px;"></div>
    <div class="square" style="left:183px; top:248px; width:13px; height:13px;"></div>
    <div class="abs contact-name" style="left:224px; top:54px;">Brett Olsen</div>
    <div class="square" style="left:223px; top:81px; width:12px; height:13px;"></div>
    <div class="abs contact-role" style="left:244px; top:81px;">Director</div>
    <div class="abs detail" style="left:222px; top:143px;">A.B.N. 37 829 516 073</div>
    <div class="abs detail" style="left:221px; top:164px;">BUILDERS LICENCE No. 573019k</div>
    <div class="square" style="left:220px; top:184px; width:13px; height:13px;"></div>
    <div class="square" style="left:199px; top:203px; width:13px; height:13px;"></div>
    <div class="abs detail" style="left:220px; top:204px;">M: 0412 907 381</div>
    <div class="square" style="left:199px; top:235px; width:13px; height:13px;"></div>
    <div class="abs detail" style="left:220px; top:236px;">E: brettolsenbuilding@mailvane.com.au</div>
  </section>

  <!-- Back, blue -->
  <section class="card card--back-blue">
    <div class="square" style="left:249px; top:128px; width:14px; height:14px; background:var(--white);"></div>
    <div class="abs brand-name" style="left:0; width:511px; top:164px; font-size:15px; color:var(--white); text-align:center;">Brett Olsen<br>Building</div>
  </section>

  <!-- Back, grey -->
  <section class="card card--back-dark">
    <div class="square" style="left:240px; top:115px; width:24px; height:24px;"></div>
    <div class="abs brand-name" style="left:0; width:510px; top:186px; font-size:27px; color:var(--ink); text-align:center;">Brett Olsen<br>Building</div>
  </section>

</div>
</body>
</html>
```